Meadowline Trail Keepers Stationary (Restricted for Brackwen)
Business Stationary
Meadowline Trail Keepers Stationary (Restricted for Brackwen) - Law
Creative Brief
Professional
Owen Halvorsk
482 W. Corliss Blvd. Suite 1700 Chicago, IL 60614
ohalvorsk@meadowlinetrailkeepers.example
www.meadowlinetrailkeepers.example
tldoverby41 tldoverby41
On #9 maybe we can removed badge and the pics of the eniors and replace with pic of kids in pool and the little boy and girl pic that you used before. I think if we using pics of seniors on insert it would look better

```html
<!DOCTYPE html>
<html lang="en">
<head>
<meta charset="utf-8">
<title>Meadowline Trail Keepers — Stationery Set</title>
<link href="https://fonts.googleapis.com/css2?family=Oswald:wght@500;700&family=Open+Sans:wght@400;600;700&display=swap" rel="stylesheet">
<style>
:root{
  --board:#3a3a3a;
  --green:#1f3b22;
  --green-dark:#15291a;
  --orange:#e0662b;
  --gold:#f1c232;
  --cream:#f6ecd7;
  --paper:#fbf8f1;
  --ink:#2d2d2d;
  --photo-a:#7fb06a;
  --photo-b:#5fa8c9;
  --photo-c:#c9a66b;
}
*{box-sizing:border-box;margin:0;padding:0}
html,body{width:1200px;height:787px;overflow:hidden;background:var(--board)}
body{position:relative;font-family:"Open Sans",Arial,sans-serif;color:var(--ink)}
.label{position:absolute;color:#fff;font:600 11px "Open Sans",Arial,sans-serif;letter-spacing:.5px}
.piece{position:absolute;overflow:hidden}
.h{font-family:"Oswald",Arial,sans-serif;font-weight:700;text-transform:uppercase;letter-spacing:.5px}
.body-text{font-size:5px;line-height:1.45}
.photo{position:absolute;background:linear-gradient(135deg,var(--photo-a),var(--photo-c))}
.photo.water{background:linear-gradient(160deg,var(--photo-b),#2f7fa6)}
.photo.round{border-radius:50%;border:3px solid var(--cream)}
.brand{display:flex;align-items:center;gap:4px;font-family:"Oswald",Arial,sans-serif;font-weight:700;text-transform:uppercase;line-height:1.05}
.brand .dot{flex:none;border-radius:50%;background:var(--gold)}
.band-orange{position:absolute;background:var(--orange);color:#fff;display:flex;align-items:center;justify-content:center}
.footer-green{position:absolute;left:0;right:0;bottom:0;background:var(--green);border-top:3px solid var(--gold)}

/* folder */
.folder-back{left:12px;top:36px;width:273px;height:384px;background:var(--green)}
.folder-back .top{position:absolute;left:0;top:0;width:100%;height:200px;background:var(--cream);padding:10px 12px}
.tab-title{display:inline-block;background:var(--green);color:#fff;font-size:8px;padding:2px 6px;margin-bottom:4px}
.folder-spine{left:285px;top:36px;width:20px;height:480px;background:var(--gold)}
.folder-spine span{position:absolute;left:50%;top:50%;transform:translate(-50%,-50%) rotate(90deg);white-space:nowrap;font-size:9px;color:var(--green-dark)}
.folder-front{left:305px;top:36px;width:283px;height:480px;background:var(--green)}
.folder-flap{left:12px;top:420px;width:273px;height:96px}

/* insert */
.insert-left{left:619px;top:36px;width:281px;height:348px;background:var(--cream)}
.insert-right{left:900px;top:36px;width:278px;height:348px;background:var(--paper);border-left:1px solid #d9cfb9}
.program{display:flex;gap:5px;align-items:flex-start}
.icon{flex:none;width:11px;height:11px;border-radius:50%;background:var(--orange)}
.program b{display:block;font-size:5.5px;color:var(--green)}
.tile{position:absolute;width:122px;height:52px}
.tile .cap{position:absolute;left:0;right:0;bottom:0;background:var(--green);color:#fff;font-size:5px;font-weight:700;padding:2px 4px;text-transform:uppercase}

/* letterhead & envelope */
.letterhead{left:696px;top:432px;width:254px;height:331px;background:var(--paper)}
.envelope{left:960px;top:600px;width:210px;height:163px;background:var(--paper)}
.watermark{position:absolute;font-family:"Oswald",Arial,sans-serif;font-weight:700;text-transform:uppercase;color:rgba(31,59,34,.07);text-align:center;line-height:1}

/* cards */
.card-front{left:67px;top:593px;width:192px;height:127px;background:var(--cream)}
.card-back{left:271px;top:593px;width:209px;height:127px;background:var(--green)}
</style>
</head>
<body>

<div class="label" style="left:168px;top:14px">FOLDER</div>
<div class="label" style="left:876px;top:14px">INSERT</div>
<div class="label" style="left:792px;top:412px">LETTERHEAD</div>
<div class="label" style="left:232px;top:570px">BUSINESS CARD</div>
<div class="label" style="left:1030px;top:582px">ENVELOPE</div>

<!-- FOLDER -->
<section class="piece folder-back">
  <div class="top">
    <div class="tab-title h">About Us</div>
    <div style="display:flex;gap:8px">
      <div class="brand" style="flex-direction:column;width:60px;font-size:7px;color:var(--green);text-align:center;gap:3px">
        <span class="dot" style="width:30px;height:30px;background:var(--green)"></span>Meadowline Trail Keepers
      </div>
      <p class="body-text">We are a team of trained rangers who protect trails, parks and open land across the county. Our crews patrol daily, guide visitors, answer calls and help keep every family safe while they enjoy the outdoors. We work with local groups, schools and city offices to care for our green spaces.</p>
    </div>
    <div class="tab-title h" style="margin-top:8px">Pledge</div>
    <p class="body-text">We pledge to serve every visitor with respect, to guard the land with care, and to answer each call for help quickly and fairly. Safety, trust and service guide our work every day on every trail we keep.</p>
  </div>
  <div style="position:absolute;left:0;top:200px;width:100%;height:184px;text-align:center;color:#fff;padding-top:18px">
    <div class="brand" style="justify-content:center;font-size:10px;color:var(--gold)"><span class="dot" style="width:22px;height:22px"></span>Meadowline Trail Keepers</div>
    <div class="h" style="font-size:10px;margin-top:18px">Contact Us</div>
    <p class="body-text" style="margin-top:4px">482 W. Corliss Blvd. Suite 1700<br>Chicago, IL 60614<br>Phone: 888-555-0147</p>
    <p style="font-size:5.5px;margin-top:6px;color:var(--gold)">www.meadowlinetrailkeepers.example</p>
  </div>
</section>

<section class="piece folder-spine"><span class="h">Park Patrol ★ Rule Enforcement ★ Park Patrol</span></section>

<section class="piece folder-front">
  <div class="photo round" role="img" aria-label="Photo of older adults enjoying a park" style="left:30px;top:14px;width:110px;height:110px"></div>
  <div class="photo round water" role="img" aria-label="Photo of children at a playground" style="left:160px;top:8px;width:92px;height:92px"></div>
  <div class="photo round" role="img" aria-label="Photo of a family picnic in the park" style="left:24px;top:150px;width:96px;height:96px"></div>
  <div class="photo round" role="img" aria-label="Photo of kids playing on park equipment" style="left:120px;top:120px;width:150px;height:150px"></div>
  <div class="band-orange h" style="left:0;top:384px;width:100%;height:28px;font-size:14px">Keeping Our Parks Safe</div>
  <p style="position:absolute;left:0;right:0;top:430px;text-align:center;color:#fff;font-size:7px">www.meadowlinetrailkeepers.example</p>
  <div class="footer-green" style="height:12px;border-top:0;background:var(--gold)"></div>
</section>

<svg class="piece folder-flap" viewBox="0 0 273 96" aria-hidden="true">
  <path d="M0 0H273V70L250 96H20L0 76Z" fill="var(--green-dark)"/>
  <path d="M0 0H273" stroke="var(--gold)" stroke-width="2"/>
  <path d="M120 0L132 10H142L154 0" fill="var(--board)"/>
</svg>

<!-- INSERT -->
<section class="piece insert-left">
  <div style="position:absolute;left:0;top:0;width:100%;height:140px;background:var(--green)"></div>
  <div class="brand" style="position:absolute;left:8px;top:12px;width:72px;flex-direction:column;font-size:6.5px;color:var(--gold);text-align:center;gap:3px">
    <span class="dot" style="width:28px;height:28px"></span>Meadowline Trail Keepers
  </div>
  <div class="photo water" role="img" aria-label="Photo of children swimming in a public pool" style="left:92px;top:12px;width:180px;height:120px;border-radius:60px 0 0 60px"></div>
  <div class="band-orange h" style="left:0;top:140px;width:100%;height:17px;font-size:9px">Keeping Our Parks Safe</div>
  <div class="h" style="position:absolute;left:12px;top:163px;font-size:9px;color:var(--green)">Our Programs</div>
  <div style="position:absolute;left:12px;top:181px;width:258px;display:grid;grid-template-columns:1fr 1fr;gap:7px 12px">
    <div class="program"><span class="icon"></span><p class="body-text"><b>Education &amp; Outreach</b>Talks and walks that teach trail safety.</p></div>
    <div class="program"><span class="icon"></span><p class="body-text"><b>Trail Patrols</b>Daily rounds on paths and in parks.</p></div>
    <div class="program"><span class="icon"></span><p class="body-text"><b>Junior Rangers</b>Summer camps for young explorers.</p></div>
    <div class="program"><span class="icon"></span><p class="body-text"><b>Water Safety</b>Guards and lessons at every pool.</p></div>
    <div class="program"><span class="icon"></span><p class="body-text"><b>Event Support</b>Staff for fairs and public events.</p></div>
    <div class="program" style="flex-direction:column;align-items:flex-end;text-align:right;gap:1px">
      <span class="h" style="font-size:7px;color:var(--orange)">Call Us Today</span>
      <span class="h" style="font-size:12px;color:var(--green)">888-555-0147</span>
    </div>
  </div>
  <p style="position:absolute;left:12px;top:308px;font-size:5.5px;color:var(--green)">www.meadowlinetrailkeepers.example</p>
  <div class="footer-green" style="height:22px"></div>
</section>

<section class="piece insert-right">
  <div class="h" style="position:absolute;left:12px;top:8px;font-size:9px;color:var(--green)">What We Do!</div>
  <p class="body-text" style="position:absolute;left:12px;top:24px;width:254px">Our rangers keep parks, trails and pools safe all year long. We patrol on foot and by bike, help lost visitors, guide school groups, respond to calls and work with local teams to protect wildlife and land.</p>
  <div class="tile" style="left:12px;top:52px"><div class="photo" role="img" aria-label="Photo of a ranger boat on the lake" style="inset:0"></div><span class="cap">Lake Patrol</span></div>
  <div class="tile" style="left:144px;top:52px"><div class="photo" role="img" aria-label="Photo of seniors walking a park trail" style="inset:0"></div><span class="cap">Trail Walks</span></div>
  <div class="tile" style="left:12px;top:112px"><div class="photo water" role="img" aria-label="Photo of a ranger helping at the pool" style="inset:0"></div><span class="cap">Pool Safety</span></div>
  <div class="tile" style="left:144px;top:112px"><div class="photo" role="img" aria-label="Photo of seniors at a park event" style="inset:0"></div><span class="cap">Community Days</span></div>
  <div class="tile" style="left:12px;top:172px"><div class="photo" role="img" aria-label="Photo of a ranger talking with visitors" style="inset:0"></div><span class="cap">Visitor Help</span></div>
  <div class="tile" style="left:144px;top:172px"><div class="photo" role="img" aria-label="Photo of a park patrol vehicle" style="inset:0"></div><span class="cap">Park Patrol</span></div>
  <p class="body-text" style="position:absolute;left:12px;top:234px;width:254px">Every ranger is trained in first aid, safety and public service. We listen to our community and plan each season with care, so that every visitor can come back again and again.</p>
  <p style="position:absolute;left:12px;top:308px;font-size:5.5px;color:var(--green)">www.meadowlinetrailkeepers.example</p>
  <div class="footer-green" style="height:22px"></div>
</section>

<!-- LETTERHEAD -->
<section class="piece letterhead">
  <div class="brand" style="position:absolute;left:0;right:0;top:14px;justify-content:center;font-size:8px;color:var(--green)"><span class="dot" style="width:16px;height:16px;background:var(--green)"></span>Meadowline Trail Keepers</div>
  <div class="watermark" style="left:20px;right:20px;top:120px;font-size:28px">Meadowline<br>Trail Keepers</div>
  <div class="footer-green" style="height:34px;color:#fff;font-size:5.5px;text-align:center;padding-top:6px;line-height:1.6">
    482 W. Corliss Blvd. Suite 1700 Chicago, IL 60614 &nbsp;|&nbsp; 888-555-0147<br>
    <span style="color:var(--gold)">www.meadowlinetrailkeepers.example</span>
  </div>
</section>

<!-- ENVELOPE -->
<section class="piece envelope">
  <div style="position:absolute;left:12px;top:14px;font-size:5px;line-height:1.5;color:var(--green)">
    <b class="h" style="font-size:6px">Contact Us</b><br>482 W. Corliss Blvd. Suite 1700<br>Chicago, IL 60614
  </div>
  <div class="brand" style="position:absolute;right:12px;top:12px;font-size:6px;color:var(--green)"><span class="dot" style="width:14px;height:14px;background:var(--green)"></span>Meadowline<br>Trail Keepers</div>
  <div class="watermark" style="left:70px;right:10px;top:55px;font-size:20px">Meadowline<br>Trail Keepers</div>
  <div class="footer-green" style="height:18px"></div>
</section>

<!-- BUSINESS CARD -->
<section class="piece card-front">
  <div class="brand" style="position:absolute;left:8px;top:14px;width:48px;flex-direction:column;font-size:6px;color:var(--green);text-align:center;gap:3px">
    <span class="dot" style="width:28px;height:28px;background:var(--green)"></span>Meadowline Trail Keepers
  </div>
  <div style="position:absolute;left:64px;top:26px">
    <div style="font-size:11px;font-weight:700;color:var(--green)">Owen Halvorsk</div>
    <div style="font-size:5.5px">Title Goes Here</div>
  </div>
  <div style="position:absolute;left:64px;top:66px;font-size:4.5px;line-height:1.6">
    ohalvorsk@meadowlinetrailkeepers.example<br>
    482 W. Corliss Blvd. Suite 1700 Chicago, IL 60614<br>
    Tel: 312-555-0182 &nbsp; Cell: 888-555-0147
  </div>
  <div class="footer-green" style="height:16px"></div>
</section>

<section class="piece card-back">
  <div class="brand" style="position:absolute;left:0;right:0;top:16px;justify-content:center;font-size:8px;color:var(--gold)"><span class="dot" style="width:22px;height:22px"></span>Meadowline Trail Keepers</div>
  <div class="h" style="position:absolute;left:0;right:0;top:60px;text-align:center;font-size:13px;color:#fff">Keeping Our Parks Safe</div>
  <p style="position:absolute;left:0;right:0;top:84px;text-align:center;font-size:5.5px;color:#fff">www.meadowlinetrailkeepers.example</p>
  <div style="position:absolute;left:0;right:0;bottom:0;height:10px;background:var(--gold)"></div>
</section>

</body>
</html>
```